sales brocure for maintenance service company

come up with an eye grabbing sales brochure to highlight our services. we specialize in full facility maintenance we provide janitorial, specialized "cleanroom" cleaning. snow and ice management landscape maintenance, building and facility repair. we only work for commercial, industrial, and educational facilities. you can use some of the photos I uploaded or stock photos our colors are navy blue deep yellow baby/powder blue. I need a design that sells jobs!

```html
<!DOCTYPE html>
<html lang="en">
<head>
<meta charset="utf-8">
<title>Harborline Facilities Services – Trifold Brochure</title>
<link href="https://fonts.googleapis.com/css2?family=Roboto+Slab:wght@400;700;800&display=swap" rel="stylesheet">
<style>
  :root {
    --navy: #1d1f7a;
    --royal: #0f4fb0;
    --sky: #1e8fe0;
    --yellow: #f2d21a;
    --powder: #dcebf6;
    --mint: #cfe6e2;
    --ink: #1b1b1b;
    --page: #eef0f2;
  }
  * { margin: 0; padding: 0; box-sizing: border-box; }
  html, body { width: 1200px; height: 1120px; overflow: hidden; background: var(--page); }
  body { font-family: "Roboto Slab", serif; position: relative; }

  .brochure {
    position: absolute; left: 90px; top: 165px;
    width: 1020px; height: 790px;
    display: flex;
    box-shadow: 0 18px 40px rgba(0,0,0,.18);
  }
  .panel { position: relative; width: 340px; height: 790px; overflow: hidden; }
  .panel-art { position: absolute; inset: 0; }

  .brand { position: absolute; left: 0; right: 0; text-align: center; }
  .brand-name {
    font-weight: 800; color: var(--navy); font-size: 40px; line-height: 1;
    display: inline-flex; align-items: center; gap: 10px; letter-spacing: 1px;
  }
  .brand-dot { width: 14px; height: 14px; border-radius: 50%; background: var(--yellow); display: inline-block; }
  .brand-sub {
    font-variant: small-caps; font-size: 15px; letter-spacing: 1.5px; color: #222; margin-top: 6px;
  }

  .cover .brand { top: 62px; }
  .tagline {
    position: absolute; left: 20px; right: 20px; top: 600px;
    text-align: center; color: var(--navy); font-weight: 700; font-size: 15px;
    transform: rotate(-7deg);
  }
  .pitch {
    position: absolute; left: 30px; right: 30px; top: 665px;
    text-align: center; color: var(--ink); font-weight: 700; font-size: 15.5px; line-height: 1.4;
  }

  .middle { background: radial-gradient(ellipse at 50% 50%, #1298e6 0%, #0c66c8 45%, #1a3f9e 100%); }
  .middle .brand { top: 250px; }
  .middle .brand-name { color: #fff; font-size: 42px; }
  .middle .brand-sub { color: var(--yellow); font-weight: 700; }
  .contact {
    position: absolute; left: 0; right: 0; top: 470px;
    text-align: center; color: #fff; font-size: 14px; line-height: 1.45;
  }
  .contact h3 { font-size: 15px; font-weight: 700; letter-spacing: .5px; }
  .contact .block { margin-bottom: 14px; }
  .web { color: var(--yellow); margin-top: 26px; font-size: 14.5px; }
</style>
</head>
<body>
<div class="brochure">

  <section class="panel cover cover-left">
    <svg class="panel-art" width="340" height="790" viewBox="0 0 340 790">
      <defs>
        <linearGradient id="paperL" x1="0" y1="0" x2="0" y2="1">
          <stop offset="0" stop-color="#f2f7fb"/><stop offset="1" stop-color="#e3eef7"/>
        </linearGradient>
        <linearGradient id="photoL" x1="0" y1="0" x2="0" y2="1">
          <stop offset="0" stop-color="#b9d3e6"/><stop offset=".35" stop-color="#a7a9b4"/>
          <stop offset=".65" stop-color="#4d7a3a"/><stop offset="1" stop-color="#5fa33b"/>
        </linearGradient>
      </defs>
      <rect width="340" height="790" fill="url(#paperL)"/>
      <path d="M0 170 H340 V520 Q170 575 0 620 Z" fill="url(#photoL)" role="img" aria-label="Photo of a landscaped two-storey building with trimmed shrubs and green lawn"/>
      <path d="M0 620 Q170 575 340 520 V560 Q170 615 0 660 Z" fill="var(--mint)"/>
      <path d="M0 790 V765 Q170 745 340 700 V790 Z" fill="var(--royal)"/>
    </svg>
    <div class="brand">
      <div class="brand-name"><span class="brand-dot"></span>Harborline</div>
      <div class="brand-sub">Facilities Services Milbrook, MA</div>
    </div>
    <p class="tagline">Complete Building and Ground Maintenance</p>
    <p class="pitch">Spring will be here soon...<br>really it will! let us quote your facility<br>landscape and cleaning needs.</p>
  </section>

  <section class="panel middle">
    <div class="brand">
      <div class="brand-name">Harborline</div>
      <div class="brand-sub">Facilities Services Milbrook, MA</div>
    </div>
    <div class="contact">
      <div class="block"><h3>OFFICE LOCATION</h3>1420 Orchard Hill Rd. Westvale, Ma. 01488</div>
      <div class="block"><h3>SHOP LOCATION</h3>27 Birchwood Rd. Milbrook, MA 01592</div>
      <div class="block">Email: service@harborline-fs.com<br>Phone: 555-318-0427</div>
      <div class="web">www.harborline-facility-services.com</div>
    </div>
  </section>

  <section class="panel cover cover-right">
    <svg class="panel-art" width="340" height="790" viewBox="0 0 340 790">
      <defs>
        <linearGradient id="paperR" x1="0" y1="0" x2="0" y2="1">
          <stop offset="0" stop-color="#f2f7fb"/><stop offset="1" stop-color="#e3eef7"/>
        </linearGradient>
        <linearGradient id="photoR" x1="0" y1="0" x2="0" y2="1">
          <stop offset="0" stop-color="#b9d3e6"/><stop offset=".35" stop-color="#a7a9b4"/>
          <stop offset=".65" stop-color="#4d7a3a"/><stop offset="1" stop-color="#5fa33b"/>
        </linearGradient>
      </defs>
      <rect width="340" height="790" fill="url(#paperR)"/>
      <path d="M0 170 H340 V520 Q170 575 0 620 Z" fill="url(#photoR)" role="img" aria-label="Photo of a landscaped two-storey building with trimmed shrubs and green lawn"/>
      <path d="M0 620 Q170 575 340 520 V560 Q170 615 0 660 Z" fill="var(--mint)"/>
      <path d="M0 790 V765 Q170 745 340 700 V790 Z" fill="var(--royal)"/>
    </svg>
    <div class="brand">
      <div class="brand-name"><span class="brand-dot"></span>Harborline</div>
      <div class="brand-sub">Facilities Services Milbrook, MA</div>
    </div>
    <p class="tagline">Complete Building and Ground Maintenance</p>
    <p class="pitch">Spring will be here soon...<br>really it will! let us quote your facility<br>landscape and cleaning needs.</p>
  </section>

</div>
</body>
</html>
```